We Buy Houses Website

Looking for a highly motivated and skillfull designer to design and code me a "we Buy Houses" type website. I have a potential logo, but if you think you can make a BETTER one, please do try and incorporate it in your template. I am looking for creativity, professionalism, simple yet elegant. I will need a simple form on the front of the template along with pictures I provide you of recent houses I have bought. Look at these sites for examples of the layout of the website:

http://www.brickvalehomes.example/
http://www.petrafixeshouses.example/
http://www.quickpropertyexitnow.example/

If you make me a design that blows me away, and you are dependable, you will become part of my team and in charge of the web aspect which will include designing, updating, any and all graphics and logo work, SEO, coding. If you have skills in all of these areas please make me a design and lets do business!! The name of the website will be "Lurt Takes Homes" at LurtTakesHomes.example

I have uploaded some pictures of houses that we have done, please feel free to incorporate this into the banner or the design, etc. I want them to know we buy houses in ANY condition, as is, cash, can close immediately so they can get on with their life. We have many options to help them find a solution to whatever problem they have. We are in the business of helping people.

Target Market(s)

People looking to sell their houses
people facing foreclosure, bankruptcy, death in the family, divorce, anyone that we can help
people with ugly houses that need a lot of repair

Industry/Entity Type

Business

Font styles to use
Serif
Sans Serif

Colors

Designer to choose colors to be used in the design.

Requirements
Must have
• must have a simple form on the front of the page, preferrably near the banner, with the few required fields to help someone get started putting in their interest to sell their house, view the 2 websites i put as examples to see what kind of fields it should have.

My phone number (555) 482-1937 along with a Lurt Takes Homes logo, clean simple and elegant and professional. I want a nice color scheme that is not white but professional and has a wow factor.

```html
<!DOCTYPE html>
<html lang="en">
<head>
<meta charset="utf-8">
<title>Lurt Takes Homes</title>
<link href="https://fonts.googleapis.com/css2?family=Lato:wght@400;700&display=swap" rel="stylesheet">
<style>
:root{
  --navy:#0a0e22;
  --navy-2:#11162e;
  --lime:#a9d62f;
  --lime-dark:#93bd22;
  --white:#ffffff;
  --muted:#c9cedd;
  --field:#1b2240;
  --circle:#2d3a5c;
}
*{margin:0;padding:0;box-sizing:border-box}
html,body{width:1200px;height:2757px;overflow:hidden;background:var(--navy)}
body{font-family:'Lato',sans-serif;color:var(--white);position:relative}
.site-header{position:absolute;left:0;top:0;width:1200px;height:156px;background:var(--navy);border-top:3px solid var(--lime)}
.brand{position:absolute;left:184px;top:58px;display:flex;align-items:center;gap:10px;color:var(--lime);font-size:24px;font-weight:700;letter-spacing:.5px}
.brand-mark{width:22px;height:22px;background:var(--lime)}
.contact-top{position:absolute;left:919px;top:10px;font-size:11px;font-weight:700}
.contact-top .phone{display:flex;align-items:center;gap:8px;color:var(--lime);font-size:15px;font-weight:400;margin-top:6px;margin-left:-16px}
.main-nav{position:absolute;top:74px;left:551px;font-size:12px;font-weight:700}
.main-nav a{position:absolute;white-space:nowrap;color:var(--white);text-decoration:none}
.main-nav a.active{color:var(--lime)}
.main-nav a.active::after{content:"";position:absolute;left:0;right:0;top:22px;height:2px;background:var(--lime)}
.hero{position:absolute;left:0;top:156px;width:1200px;height:414px;background:linear-gradient(180deg,#6f93c7 0%,#9bb4d1 30%,#a99d8c 55%,#5c7a3c 78%,#7a8a4a 100%)}
.hero-title{position:absolute;left:182px;top:110px;font-size:27px;font-weight:700}
.hero-rule{position:absolute;left:182px;top:158px;width:244px;height:3px;background:var(--white)}
.hero-text{position:absolute;left:182px;top:178px;width:480px;font-size:18px;font-weight:700;line-height:31px}
.hero-arrow{position:absolute;top:190px;width:28px;height:30px;background:rgba(10,14,34,.55);display:flex;align-items:center;justify-content:center}
.hero-dots{position:absolute;top:397px;left:481px;display:flex;gap:4px}
.hero-dots span{width:78px;height:3px;background:rgba(255,255,255,.5)}
.hero-dots span:first-child{background:var(--white)}
.offer-form{position:absolute;left:781px;top:35px;width:254px;height:329px;background:var(--navy);border:6px solid rgba(255,255,255,.35);background-clip:padding-box;padding:20px 30px}
.offer-form h2{font-size:15px;font-weight:700;line-height:18px}
.field{display:block;height:28px;border:1px solid #39415f;background:var(--navy);color:var(--lime);font-size:9px;padding:9px 12px;margin-bottom:12px;font-family:inherit}
.form-fields{position:absolute;left:30px;right:30px;top:78px}
.field-row{display:flex;gap:10px}
.field-row .field{flex:1}
.submit{display:block;height:28px;background:var(--lime);color:var(--white);font-size:10px;font-weight:700;text-align:center;line-height:28px}
.thumb-strip{position:absolute;left:0;top:570px;width:1200px;height:97px;display:flex}
.thumb-strip div{flex:1;border-right:2px solid var(--navy)}
.section-title{position:absolute;left:0;width:1200px;text-align:center;font-size:19px;font-weight:700}
.how{position:absolute;left:0;top:667px;width:1200px;height:415px;background:var(--navy)}
.step{position:absolute;top:163px;width:240px;text-align:center}
.step-icon{width:96px;height:96px;border-radius:50%;background:var(--circle);margin:0 auto;overflow:hidden}
.step h3{font-size:13px;font-weight:400;margin-top:26px}
.step p{font-size:11px;margin-top:17px;color:var(--white)}
.houses{position:absolute;left:0;top:1082px;width:1200px;height:434px;background:var(--lime)}
.houses .section-title{top:85px}
.house-list{position:absolute;top:162px;width:196px;list-style:none}
.house-list li{height:39px;border-bottom:1px solid rgba(255,255,255,.35);font-size:11px;display:flex;align-items:center;gap:17px}
.house-list li::before{content:"›";width:16px;height:16px;border:1px solid var(--white);border-radius:50%;font-size:12px;line-height:13px;text-align:center}
.house-photo{position:absolute;top:166px;width:192px;height:127px;border:2px solid var(--white)}
.btn-outline{position:absolute;left:908px;top:368px;width:108px;height:29px;border:1px solid var(--white);font-size:10px;text-align:center;line-height:27px}
.testimonials{position:absolute;left:0;top:1516px;width:1200px;height:358px;background:var(--navy)}
.testimonials .section-title{top:85px}
.quote{position:absolute;left:0;top:146px;width:1200px;text-align:center;font-size:11px;line-height:18px;white-space:nowrap}
.quote-open{position:absolute;left:230px;top:140px;color:var(--lime);font-size:40px;font-weight:700;line-height:1}
.quote-close{display:inline-block;color:var(--lime);font-size:40px;font-weight:700;line-height:0;vertical-align:-20px;margin-left:8px}
.author{position:absolute;left:556px;top:236px;display:flex;align-items:center;gap:14px;font-size:11px}
.avatar{width:34px;height:34px;border-radius:50%;background:#c9a98c}
.author .name{color:var(--lime)}
.author .role{color:var(--muted);margin-top:4px}
.testi-arrow{position:absolute;top:244px}
.articles{position:absolute;left:0;top:1874px;width:1200px;height:552px;background:var(--lime)}
.articles .section-title{top:88px}
.article{position:absolute;top:166px;width:263px}
.article-photo{height:147px}
.article h3{text-align:center;font-size:12px;font-weight:400;margin-top:25px}
.article p{text-align:center;font-size:10px;line-height:18px;margin-top:12px;padding:0 4px}
.article-meta{margin-top:22px;border-top:1px solid rgba(255,255,255,.4);border-bottom:1px solid rgba(255,255,255,.4);height:22px;display:flex;justify-content:space-between;align-items:center;font-size:9px;padding:0 2px}
.site-footer{position:absolute;left:0;top:2426px;width:1200px;height:285px;background:linear-gradient(180deg,#131a33,#0a0e22 70%)}
.footer-col{position:absolute;top:28px;width:190px;font-size:10px;line-height:16px}
.footer-col h4{font-size:12px;font-weight:400;margin-bottom:16px;display:flex;align-items:center;gap:10px}
.post{display:flex;gap:10px;margin-bottom:6px}
.post-thumb{width:48px;height:40px;background:#6b6a62;flex:none}
.newsletter-input{display:flex;gap:6px;margin-top:18px}
.newsletter-input span{border:1px solid var(--white);height:24px;font-size:9px;padding:5px 8px}
.contact-line{display:flex;align-items:center;gap:8px}
.bottom-bar{position:absolute;left:0;top:2711px;width:1200px;height:46px;background:var(--lime);font-size:9px}
.bottom-bar .copy{position:absolute;left:184px;top:17px}
.social{position:absolute;left:886px;top:12px;display:flex;gap:16px}
.social span{width:20px;height:20px;border:1px solid var(--white)}
</style>
</head>
<body>

<header class="site-header">
  <div class="brand"><span class="brand-mark"></span>Lurt Takes Homes</div>
  <div class="contact-top">Contact Us Today:
    <div class="phone">
      <svg width="10" height="12" viewBox="0 0 10 12"><path d="M2 0l2 3-1 1.5c.6 1.6 1.6 2.8 3 3.5L7.5 7 10 9l-1.5 2.5C4 11 1 6.5 0 1.5z" fill="#a9d62f"/></svg>
      (555) 482-1937</div>
  </div>
  <nav class="main-nav">
    <a class="active" style="left:0">Home</a>
    <a style="left:54px">About</a>
    <a style="left:109px">How It Works</a>
    <a style="left:204px">Sell a House</a>
    <a style="left:291px">Testimonials</a>
    <a style="left:377px">Blog</a>
    <a style="left:423px">Contact</a>
  </nav>
</header>

<section class="hero" role="img" aria-label="Blurred photo of a single-storey house with lawn and driveway">
  <h1 class="hero-title">Sell Your House Fast</h1>
  <div class="hero-rule"></div>
  <p class="hero-text">Selling your house can be simple, let us show you how we have changed the way you can sell your house.</p>
  <div class="hero-arrow" style="left:87px"><svg width="8" height="12"><path d="M7 1L2 6l5 5" stroke="#fff" stroke-width="2" fill="none"/></svg></div>
  <div class="hero-arrow" style="left:1083px"><svg width="8" height="12"><path d="M1 1l5 5-5 5" stroke="#fff" stroke-width="2" fill="none"/></svg></div>
  <div class="hero-dots"><span></span><span></span><span></span></div>

  <form class="offer-form">
    <h2>Get An Offer<br>On Your House</h2>
    <div class="form-fields">
      <span class="field">Name</span>
      <span class="field">Phone Number</span>
      <span class="field">Your Email</span>
      <span class="field">Property Adress</span>
      <div class="field-row"><span class="field">City</span><span class="field">Zip Code</span></div>
      <span class="submit">SUBMIT</span>
    </div>
  </form>
</section>

<div class="thumb-strip" role="img" aria-label="Row of photos of recently bought houses: kitchens, bathrooms, empty rooms, a patio and a front yard">
  <div style="background:linear-gradient(#7a5a3c,#4a3526)"></div>
  <div style="background:linear-gradient(#5a4030,#2c2018)"></div>
  <div style="background:linear-gradient(#8a6a4a,#4e3826)"></div>
  <div style="background:linear-gradient(#6a5e58,#4a3e38)"></div>
  <div style="background:linear-gradient(#b8a89a,#8a4a44)"></div>
  <div style="background:linear-gradient(#9a8a78,#6a5a48)"></div>
  <div style="background:linear-gradient(#cfd8e0,#8a7a5a)"></div>
  <div style="background:linear-gradient(#5a8ad0,#7a9a5a)"></div>
</div>

<section class="how">
  <h2 class="section-title" style="top:87px">How It Works...</h2>
  <div class="step" style="left:157px">
    <div class="step-icon"><svg width="96" height="96"><path d="M48 48l48 48H48z" fill="#243050"/><path d="M34 60l4-10 16-16 6 6-16 16z" fill="#f2b632"/><path d="M54 34l4-4 6 6-4 4z" fill="#e0566a"/><path d="M34 60l2-6 4 4z" fill="#2b2b2b"/></svg></div>
    <h3>Complete the Form</h3><p>We evaluate your property instantly.</p>
  </div>
  <div class="step" style="left:372px">
    <div class="step-icon"><svg width="96" height="96"><path d="M48 48l48 48H48z" fill="#243050"/><rect x="37" y="28" width="22" height="40" rx="3" fill="#fff"/><rect x="40" y="33" width="16" height="27" fill="#2d3a5c"/><circle cx="48" cy="64" r="2" fill="#2d3a5c"/></svg></div>
    <h3>Get a Call within 24 Hours</h3><p>We can discuss your best options.</p>
  </div>
  <div class="step" style="left:586px">
    <div class="step-icon"><svg width="96" height="96"><path d="M48 48l48 48H48z" fill="#243050"/><circle cx="48" cy="42" r="12" fill="#f5d34a"/><rect x="43" y="52" width="10" height="10" fill="#e8e8e8"/><rect x="44" y="62" width="8" height="3" fill="#9aa"/></svg></div>
    <h3>Find a Solution</h3><p>Sell your house fast.</p>
  </div>
  <div class="step" style="left:799px">
    <div class="step-icon"><svg width="96" height="96"><path d="M48 48l48 48H48z" fill="#243050"/><rect x="28" y="36" width="40" height="24" fill="#4aa65a"/><rect x="32" y="40" width="32" height="16" fill="none" stroke="#8fd49a" stroke-width="1.5"/><circle cx="48" cy="48" r="5" fill="#8fd49a"/></svg></div>
    <h3>Go On With Your Life</h3><p>Find the relief you deserve.</p>
  </div>
</section>

<section class="houses">
  <h2 class="section-title">Houses that we buy</h2>
  <ul class="house-list" style="left:184px">
    <li>Normal Homes</li><li>Vacant Homes</li><li>Needs Repairs</li><li>Needs Extensive Renovation</li><li>Has Suffered Storm Damage</li>
  </ul>
  <ul class="house-list" style="left:399px;width:190px">
    <li>Undesirable Neighborhood</li><li>Bad Tenants</li><li>Code Violations</li><li>Relocation Or Emigration</li><li>Has Become Too Ugly To Sell</li>
  </ul>
  <div class="house-photo" style="left:610px;background:linear-gradient(#d8cfc4,#8a7060)" role="img" aria-label="Room under repair with patched drywall"></div>
  <div class="house-photo" style="left:825px;background:linear-gradient(#a88258,#4a3020)" role="img" aria-label="Renovated kitchen with wooden cabinets"></div>
  <div class="btn-outline">View Our Gallery</div>
</section>

<section class="testimonials">
  <h2 class="section-title">Testimonials</h2>
  <span class="quote-open">“</span>
  <p class="quote">Phasellus varius felis magna, id dapibus dui luctus et. Nam molestie ac eros sed eleifend. Etiam porttitor varius venenatis. Integer<br>dui ante, euismod sed condimentum sit amet, lobortis et enim. Proin in felis ornare, aliquet justo non, feugiat dui.<br>Sed consequat odio quis faucibus rutrum. Vestibulum porta nunc tellus, in lacinia nisl malesuada sed.<span class="quote-close">”</span></p>
  <svg class="testi-arrow" style="left:506px" width="12" height="18"><path d="M10 2L3 9l7 7" stroke="#fff" stroke-width="2" fill="none"/></svg>
  <div class="author"><div class="avatar" role="img" aria-label="Client portrait"></div><div><div class="name">Dale Morrow</div><div class="role">Client</div></div></div>
  <svg class="testi-arrow" style="left:708px" width="12" height="18"><path d="M2 2l7 7-7 7" stroke="#fff" stroke-width="2" fill="none"/></svg>
</section>

<section class="articles">
  <h2 class="section-title">Latest Articles</h2>
  <article class="article" style="left:184px">
    <div class="article-photo" style="background:linear-gradient(#c8ccd0 40%,#8a7a5a 75%,#7a6a50)" role="img" aria-label="House with front yard"></div>
    <h3>Proin venenatis leo dui</h3>
    <p>Praesent elementum faucibus sapien. Nunc blandit tellus et odio volutpat elementum sed ut turpis. Praesent sit amet varius sem.</p>
    <div class="article-meta"><span>◷ 18 June 2014</span><span>✎ Admin</span><span>▭ 2 Comments</span></div>
  </article>
  <article class="article" style="left:469px">
    <div class="article-photo" style="background:linear-gradient(#e8e4dc 30%,#6a6a4a 70%,#5a5040)" role="img" aria-label="Covered patio with overgrown yard"></div>
    <h3>Proin venenatis leo dui</h3>
    <p>Praesent elementum faucibus sapien. Nunc blandit tellus et odio volutpat elementum sed ut turpis. Praesent sit amet varius sem.</p>
    <div class="article-meta"><span>◷ 18 June 2014</span><span>✎ Admin</span><span>▭ 2 Comments</span></div>
  </article>
  <article class="article" style="left:753px">
    <div class="article-photo" style="background:linear-gradient(90deg,#c8b8a8,#4a3a30 50%,#d8d0c8)" role="img" aria-label="Renovated bathroom with dark tiles"></div>
    <h3>Proin venenatis leo dui</h3>
    <p>Praesent elementum faucibus sapien. Nunc blandit tellus et odio volutpat elementum sed ut turpis. Praesent sit amet varius sem.</p>
    <div class="article-meta"><span>◷ 18 June 2014</span><span>✎ Admin</span><span>▭ 2 Comments</span></div>
  </article>
</section>

<footer class="site-footer">
  <div class="footer-col" style="left:184px">
    <h4>About <svg width="12" height="12"><circle cx="6" cy="4" r="3" fill="#a9d62f"/><path d="M0 12a6 5 0 0112 0z" fill="#a9d62f"/></svg></h4>
    <p>Mauris gravida, nibh at vulputate mattis, diam urna aliquam ante, sit amet blandit magna dui sed nisi. Phasellus interdum sollicitudin euismod. Vestibulum a tortor eleifend, luctus purus at, placerat leo.</p>
  </div>
  <div class="footer-col" style="left:397px">
    <h4>Latest Posts <svg width="12" height="12"><path d="M1 11l2-5 6-6 3 3-6 6z" fill="#a9d62f"/></svg></h4>
    <div class="post"><div class="post-thumb" role="img" aria-label="House thumbnail"></div><div>Proin venenatis leo dui<br>Posted 18 June 2014</div></div>
    <div class="post"><div class="post-thumb" role="img" aria-label="House thumbnail"></div><div>Suspendisse sed aliquet ante<br>Posted 18 June 2014</div></div>
    <div class="post"><div class="post-thumb" role="img" aria-label="House thumbnail"></div><div>Lorem ipsum dolor sit amet<br>Posted 18 June 2014</div></div>
  </div>
  <div class="footer-col" style="left:610px">
    <h4>Newsletter <svg width="12" height="12"><path d="M0 5L12 0 7 12 6 6z" fill="#a9d62f"/></svg></h4>
    <p>Phasellus interdum sollicitudin euismod. Vestibulum a tortor eleifend, luctus purus at, placerat leo.</p>
    <div class="newsletter-input"><span style="width:152px">Email adress...</span><span>OK</span></div>
  </div>
  <div class="footer-col" style="left:823px;width:210px">
    <h4>Get in Touch <svg width="13" height="11"><ellipse cx="6" cy="5" rx="6" ry="4.5" fill="#a9d62f"/></svg></h4>
    <p>Lurt Takes Homes<br>812 Alder Crest Way, Suite B4<br>Marlow Bay, CA 90021</p>
    <p class="contact-line" style="margin-top:4px"><svg width="9" height="10" viewBox="0 0 10 12"><path d="M2 0l2 3-1 1.5c.6 1.6 1.6 2.8 3 3.5L7.5 7 10 9l-1.5 2.5C4 11 1 6.5 0 1.5z" fill="#a9d62f"/></svg>(555) 482-1937</p>
    <p class="contact-line"><svg width="10" height="8"><rect width="10" height="8" fill="#a9d62f"/></svg>contact@lurttakeshomes.example</p>
  </div>
</footer>

<div class="bottom-bar">
  <span class="copy">©2014 Lurt Takes Homes - All Rights Reserved. &nbsp; Privacy policy &nbsp;|&nbsp; Terms of services</span>
  <div class="social"><span></span><span></span><span></span><span></span></div>
</div>

</body>
</html>
```